General Contractors need a new Crisp updated Card Design

We need a new business card design for our company of 25 years based in Toronto call Pollvarn Building Inc. : Our goal is to be the leading commercial contractors in Toronto by providing exceptional value to our clients. We work very hard to deliver professional, quality, service in conjunction with consistent price competitiveness to all of our clients on every single project.

Target Market(s)

Design & Build Clients

Industry/Entity Type

Construction Company

Contact Information for Business Card

Address:
18 West Marlow Field Road, Unit 17, Dunmore Vale, ON, K7T 2M9
Office: 905-218-6937

Pollvarns Logo
Employee Job Description
Employee Cell Phone #
Employee Email
www.pollvarn.example

Colors

Designer to choose colors to be used in the design.

Requirements
Must have
• Quote Company Saying:
• "Professional. Quality. Service."
Nice to have
• New Crisp up to date look. simple & fresh ( Not to Busy)
Should not have
• NO BLUE PRINTS ON THE BUSINESS CARDS

```html
<!DOCTYPE html>
<html lang="en">
<head>
<meta charset="UTF-8">
<title>Pollvarn Building Inc. – Business Card</title>
<link href="https://fonts.googleapis.com/css2?family=Roboto:wght@400;500&family=Tinos&display=swap" rel="stylesheet">
<style>
  :root {
    --page-bg: #2b2b2b;
    --card-bg: #1c1c1d;
    --card-edge: #262627;
    --brand-teal: #0f8a76;
    --tagline: #e6e6e6;
    --silver-light: #d9d9d9;
    --silver-dark: #8a8a8a;
    --text-soft: #c9c9c9;
    --text-muted: #9a9a9a;
    --divider: #777777;
  }
  * { margin: 0; padding: 0; box-sizing: border-box; }
  html, body {
    width: 1200px;
    height: 900px;
    overflow: hidden;
    background: var(--page-bg);
  }
  .canvas {
    position: relative;
    width: 1200px;
    height: 900px;
  }
  .card {
    position: absolute;
    left: 250px;
    width: 700px;
    height: 400px;
    background: var(--card-bg);
    border: 1px solid var(--card-edge);
    border-radius: 22px;
    box-shadow: 0 10px 26px rgba(0,0,0,0.45);
  }
  .card-front { top: 35px; }
  .card-back { top: 465px; }

  /* Front */
  .brand {
    position: absolute;
    top: 120px;
    left: 0;
    width: 100%;
    display: flex;
    justify-content: center;
    align-items: center;
    gap: 20px;
  }
  .brand-square {
    width: 62px;
    height: 62px;
    background: var(--brand-teal);
  }
  .brand-name {
    font-family: "Tinos", "Times New Roman", serif;
    font-size: 44px;
    color: var(--brand-teal);
    letter-spacing: 1px;
  }
  .tagline {
    position: absolute;
    top: 250px;
    width: 100%;
    text-align: center;
    font-family: "Tinos", "Times New Roman", serif;
    font-size: 27px;
    color: var(--tagline);
    letter-spacing: 0.5px;
  }

  /* Back */
  .person {
    position: absolute;
    top: 128px;
    right: 380px;
    text-align: right;
    font-family: "Roboto", Arial, sans-serif;
  }
  .person-name {
    font-size: 42px;
    font-weight: 500;
    letter-spacing: 1px;
    line-height: 1;
    background: linear-gradient(90deg, var(--silver-dark), var(--silver-light) 55%, #ffffff);
    -webkit-background-clip: text;
    background-clip: text;
    color: transparent;
  }
  .person-title {
    margin-top: 8px;
    font-size: 20px;
    letter-spacing: 3px;
    color: var(--text-soft);
  }
  .divider {
    position: absolute;
    left: 350px;
    top: 112px;
    width: 1px;
    height: 110px;
    background: var(--divider);
  }
  .contacts {
    position: absolute;
    left: 375px;
    top: 118px;
    list-style: none;
    font-family: "Roboto", Arial, sans-serif;
    font-size: 19px;
    color: var(--text-soft);
  }
  .contacts li {
    display: flex;
    align-items: center;
    gap: 12px;
    height: 24px;
  }
  .contacts svg {
    width: 15px;
    height: 15px;
    fill: var(--text-soft);
    flex: none;
  }
  .address {
    position: absolute;
    top: 302px;
    width: 100%;
    text-align: center;
    font-family: "Roboto", Arial, sans-serif;
    font-size: 19px;
    line-height: 1.3;
    color: var(--text-muted);
  }
</style>
</head>
<body>
<main class="canvas">
  <section class="card card-front">
    <div class="brand">
      <div class="brand-square"></div>
      <div class="brand-name">Pollvarn Building Inc.</div>
    </div>
    <p class="tagline">Professional. Quality. Service.</p>
  </section>

  <section class="card card-back">
    <div class="person">
      <div class="person-name">MARCUS HALE</div>
      <div class="person-title">CEO/FOUNDER</div>
    </div>
    <div class="divider"></div>
    <ul class="contacts">
      <li>
        <svg viewBox="0 0 16 16" aria-hidden="true"><path d="M3.5 1l3 3-1.6 1.8a9 9 0 0 0 5.3 5.3L12 9.5l3 3-2 2.3C7 14.5 1.5 9 1.2 3z"/></svg>
        905-218-6937
      </li>
      <li>
        <svg viewBox="0 0 16 16" aria-hidden="true"><path d="M4 0h8a1 1 0 0 1 1 1v14a1 1 0 0 1-1 1H4a1 1 0 0 1-1-1V1a1 1 0 0 1 1-1zm1 2v10h6V2zm3 11a1 1 0 1 0 0 2 1 1 0 0 0 0-2z"/></svg>
        905-218-7402
      </li>
      <li>
        <svg viewBox="0 0 16 16" aria-hidden="true"><path d="M1 3h14v10H1zm1.5 1.2v.4L8 8.5l5.5-3.9v-.4zM2.5 6.2V11.8h11V6.2L8 10.1z"/></svg>
        info@pollvarn.example
      </li>
      <li>
        <svg viewBox="0 0 16 16" aria-hidden="true"><path d="M8 1a7 7 0 1 0 0 14A7 7 0 0 0 8 1zm0 1.5c.9 0 1.9 1.6 2.2 4.3H5.8C6.1 4.1 7.1 2.5 8 2.5zM2.6 7h2.2c0 .9.1 1.6.2 2.5H2.8A5.5 5.5 0 0 1 2.6 7zm8.6 0h2.2a5.5 5.5 0 0 1-.2 2.5H11c.1-.9.2-1.6.2-2.5zM5.4 11h5.2c-.4 1.6-1.3 2.5-2.6 2.5S5.8 12.6 5.4 11z"/></svg>
        www.pollvarn.example
      </li>
    </ul>
    <p class="address">18 West Marlow Field Road<br>Unit 17, Dunmore Vale, ON, K7T 2M9</p>
  </section>
</main>
</body>
</html>
```